Design Direction Exploration for Brand Deliverables

Here is the link to the finalized logo. If you have a design in this project, please use this version of the logo.

https://files.dropvault.example/get/QmRtYpLsNw

Here's the new web address: coralreedtalent.example

I need a business card, a LinkedIn Business Banner, a set of slides ("Opening Title slide and the "Thank You" slide), and two social media posts created in accordance with the current brand guidelines for "CoralReed Voice Talent | For the Rivers Trade". These deliverables should be made within Canva so I can use them.

Target Market(s)

Professionals in the water sector. CoralReed is a curated platform that connects water-focused organizations—NGOs, environmental firms, public utilities, and innovators—with exceptional voice actors. Our aim is to elevate the use of voice in storytelling across the water sector, from documentaries and e-learning to product launches and advocacy campaigns. This model puts voice actors first while also responding to a sector with growing communication needs.

Industry/Entity Type

CoralReed Voice Talent | For the Rivers Trade is the go-to authority in voice talent for the global water industry. Unlike traditional agencies, CoralReed operates as a highly curated platform, connecting water and environment-focused firms, organizations, innovators, and advocates with exceptional human voice actors who bring clarity, credibility, and impact to their communication. From documentaries and promos to e-learning and product launches, our talent delivers performances at industry rates that engage audiences and elevate the stories shaping the future of water. By focusing exclusively on the water sector, CoralReed ensures every client gains not only access to world-class voice actors but also a partner who understands the urgency and importance of their mission.

Font styles to use
Other font styles liked:
• See brand guidelines.

Colors

Designer to choose colors to be used in the design.

Requirements
Must have
• The elements of the three page brand guidelines: typeface, color palette, secondary element, and recommendation on photo usage.
Nice to have
• Use the three-page brand guidelines to influence your work. The products should feel high-end, inspirational, modern. If it were a home, it would be featured in Interior Ledger. If it were a specific look, it would be featured in Plume. It's the Valtoria of voice talent. Luxurious, trustworthy, the go-to authority. I like some dimensionality/watermarks.
Should not have
• Cheap looking anything. The brand guidelines is a placeholder that I put together. I will update it based on what design this project yields.

```html
<!DOCTYPE html>
<html lang="en">
<head>
<meta charset="utf-8">
<title>CoralReed Voice Talent – Launch Post</title>
<link rel="stylesheet" href="https://fonts.googleapis.com/css2?family=Poppins:wght@400;600&display=swap">
<style>
  :root {
    --sky-top: #b8cffc;
    --sky-mid: #bfe3ee;
    --mint-low: #c8f3e0;
    --ink: #1f4744;
    --brand: #1f6ea6;
    --wave-1: #a6dfe6;
    --wave-2: #8ccde6;
    --wave-3: #66b6e8;
    --wave-4: #3d94e2;
    --wave-deep: #6fb0ea;
    --photo-warm: #d9cfc4;
    --photo-cool: #9fb3c2;
  }
  * { margin: 0; padding: 0; box-sizing: border-box; }
  html, body { width: 1200px; height: 1200px; overflow: hidden; }
  body { font-family: "Poppins", sans-serif; }

  .post {
    position: relative;
    width: 1200px;
    height: 1200px;
    overflow: hidden;
    background: linear-gradient(180deg, var(--sky-top) 0%, var(--sky-mid) 50%, var(--mint-low) 78%);
  }

  .brand-mark {
    position: absolute;
    top: 66px;
    left: 0;
    width: 100%;
    display: flex;
    justify-content: center;
    align-items: center;
    gap: 12px;
  }
  .brand-mark__dot {
    width: 22px;
    height: 22px;
    border-radius: 50%;
    background: var(--brand);
  }
  .brand-mark__name {
    font-weight: 600;
    font-size: 26px;
    color: var(--brand);
    letter-spacing: 0.2px;
  }

  .hero-photo {
    position: absolute;
    left: 344px;
    top: 161px;
    width: 512px;
    height: 395px;
  }

  .caption {
    position: absolute;
    top: 622px;
    left: 150px;
    width: 900px;
    text-align: center;
    color: var(--ink);
    font-size: 22px;
    line-height: 33px;
    font-weight: 400;
  }
  .caption p + p { margin-top: 33px; }

  .waves {
    position: absolute;
    left: 0;
    bottom: 0;
    width: 1200px;
    height: 300px;
  }
  .base-line {
    position: absolute;
    left: 0;
    bottom: 0;
    width: 100%;
    height: 8px;
    background: var(--mint-low);
  }
</style>
</head>
<body>
  <main class="post">
    <header class="brand-mark">
      <span class="brand-mark__dot"></span>
      <span class="brand-mark__name">CoralReed Voice Talent</span>
    </header>

    <svg class="hero-photo" viewBox="0 0 512 395" role="img" aria-label="Photo of two professional women reviewing documents together at a café table">
      <defs>
        <linearGradient id="photoTone" x1="0" y1="0" x2="1" y2="1">
          <stop offset="0" stop-color="var(--photo-warm)"/>
          <stop offset="0.55" stop-color="#c9c4c0"/>
          <stop offset="1" stop-color="var(--photo-cool)"/>
        </linearGradient>
      </defs>
      <g fill="url(#photoTone)">
        <rect x="0" y="0" width="174" height="395" rx="87"/>
        <rect x="169" y="0" width="174" height="395" rx="87"/>
        <rect x="338" y="0" width="174" height="395" rx="87"/>
      </g>
    </svg>

    <section class="caption">
      <p>"Are you a voice actor looking for purpose-driven projects? Or an organization in the water sector in need of a powerful voice for your next campaign? CoralReed is the platform built for you. We curate talent and connect causes.</p>
      <p>Visit our website to explore the possibilities and make your voice heard. Link in bio! #CoralReedLaunch #VoiceTalent #WaterIndustry #GetHeard"</p>
    </section>

    <svg class="waves" viewBox="0 0 1200 300" preserveAspectRatio="none" aria-hidden="true">
      <defs>
        <linearGradient id="deepWater" x1="0" y1="0" x2="0" y2="1">
          <stop offset="0" stop-color="var(--wave-4)"/>
          <stop offset="1" stop-color="var(--wave-deep)"/>
        </linearGradient>
      </defs>
      <path fill="var(--wave-1)" d="M0 40 C120 10 220 60 360 40 S600 10 760 38 S1020 60 1120 20 L1200 5 L1200 300 L0 300 Z"/>
      <path fill="var(--wave-2)" d="M0 70 C140 45 260 95 420 70 S700 40 860 68 S1080 85 1200 35 L1200 300 L0 300 Z"/>
      <path fill="var(--wave-3)" d="M0 100 C150 78 300 120 460 98 S760 72 920 98 S1100 110 1200 70 L1200 300 L0 300 Z"/>
      <path fill="url(#deepWater)" d="M0 130 C160 110 320 148 480 128 S780 105 940 130 S1110 135 1200 105 L1200 300 L0 300 Z"/>
    </svg>
    <div class="base-line"></div>
  </main>
</body>
</html>
```